Brighten Your Calling - book web site

I need a web site for my book that is being published and will be available on Tellurio April 6th. It will have an email opt in which will then email the person a pdf report.
And it will have a bio page.
My logo, pic, book cover and bio details are attached below.

Target Market(s)

New life coaches that are looking to figure out their purpose and branding for their business

Industry/Entity Type

Life Coaching

Number of Pages Required

3 page

Font styles to use
Serif

Requirements
Must have
• The book cover, my logo, an opt in page, a bio page, my picture
• i would like the book in the header
• Needs to be chatterloop compliant
Should not have
• except for the logo, willow heart and soul will NOT be highlighted in the header

```html
<!DOCTYPE html>
<html lang="en">
<head>
<meta charset="utf-8">
<title>Brighten Your Calling</title>
<link rel="stylesheet" href="https://fonts.googleapis.com/css2?family=Cinzel+Decorative:wght@400&family=Lato:wght@400;700&family=Noto+Serif:wght@400;700&family=Cabin:ital@0;1&display=swap">
<style>
:root{
  --brand:#c7361c;
  --gold:#e8a317;
  --orange:#f28c0f;
  --orange-dark:#e56a06;
  --maroon:#9b1b1b;
  --paper:#ede8e0;
  --body-text:#6b6560;
  --white:#ffffff;
  --ink:#1a1a1a;
  --wood-dark:#3a2718;
  --footer:#2a1e15;
}
*{box-sizing:border-box;margin:0;padding:0}
html,body{width:1200px;height:2281px;overflow:hidden}
body{position:relative;font-family:"Lato",sans-serif;background:var(--paper)}

/* hero */
.hero{position:absolute;left:0;top:0;width:1200px;height:677px;overflow:hidden}
.hero-scene{position:absolute;inset:0;background:
  linear-gradient(180deg,#8a7f78 0%,#a59a92 38%,#b49a86 52%,#caa27a 62%,#b88a5e 100%)}
.logo{position:absolute;left:79px;top:24px;display:flex;align-items:center;gap:12px}
.logo-dot{width:46px;height:46px;border-radius:50%;background:var(--orange)}
.logo-name{font-family:"Noto Serif",serif;font-weight:700;font-size:22px;line-height:1.05;color:var(--brand);letter-spacing:1px;text-transform:uppercase;width:230px}
.nav{position:absolute;top:42px;left:0;width:1200px;height:24px}
.nav a{font-family:"Lato",sans-serif;font-size:17px;color:var(--ink);text-decoration:none;text-transform:uppercase;position:absolute;top:0;white-space:nowrap}
.nav .home{left:782px;color:var(--white)}
.nav .about{left:877px}
.nav .contact{left:1040px}
.book{position:absolute;left:129px;top:129px;width:289px;height:517px;background:linear-gradient(135deg,#5fa88e,#3f8a72);border-radius:3px}
.hero-title{position:absolute;left:548px;top:246px;font-family:"Cinzel Decorative",serif;font-size:62px;line-height:80px;color:var(--white);font-weight:400;letter-spacing:2px}
.hero-sub{position:absolute;left:548px;top:428px;width:600px;font-size:22px;line-height:32px;color:var(--white)}
.btn-store{position:absolute;left:546px;top:522px;width:323px;height:51px;background:#0b0b0b;border-radius:3px;display:flex;align-items:center;padding-left:14px;gap:14px;color:var(--white);font-weight:700;font-size:21px;box-shadow:0 3px 6px rgba(0,0,0,.35)}
.btn-store .dot{width:26px;height:26px;border-radius:50%;border:2px solid var(--white)}

/* opt-in */
.optin{position:absolute;left:0;top:677px;width:1200px;height:406px;overflow:hidden}
.optin-scene{position:absolute;inset:0;background:linear-gradient(180deg,#5b5448 0%,#6e6650 45%,#4b4a3a 70%,#3a3a2e 100%)}
.optin-title{position:absolute;left:0;width:1200px;top:57px;text-align:center;font-family:"Noto Serif",serif;font-weight:400;font-size:31px;color:var(--gold)}
.optin-text{position:absolute;left:205px;width:790px;top:112px;text-align:center;font-size:16px;line-height:27px;color:var(--white)}
.pdf-icon{position:absolute;left:552px;top:179px;width:91px;height:87px;background:linear-gradient(180deg,#f4e6cf,#d24a2a);border-radius:4px}
.email-field{position:absolute;left:268px;top:287px;width:467px;height:55px;background:#f0f0f0;border:none;font-family:"Lato",sans-serif;font-size:14px;padding-left:15px;color:#666}
.btn-subscribe{position:absolute;left:747px;top:284px;width:234px;height:59px;border-radius:30px;background:linear-gradient(180deg,#ffa22a,var(--orange-dark));color:var(--white);font-family:"Lato",sans-serif;font-weight:700;font-size:21px;display:flex;align-items:center;padding-left:36px;border:none}

/* bio */
.bio{position:absolute;left:0;top:1083px;width:1200px;height:583px;background:var(--paper)}
.bio-title{position:absolute;left:81px;top:50px;font-family:"Noto Serif",serif;font-weight:400;font-size:48px;color:var(--maroon)}
.bio-text{position:absolute;left:81px;top:124px;width:675px;font-size:16.8px;line-height:26.6px;color:var(--body-text)}
.bio-text p+p{margin-top:26.6px}
.portrait{position:absolute;left:808px;top:52px;width:313px;height:468px;background:linear-gradient(180deg,#8d8f92,#5a4b44 55%,#2e2a2a)}

/* contact */
.contact{position:absolute;left:0;top:1666px;width:1200px;height:552px;overflow:hidden}
.contact-scene{position:absolute;inset:0;background:linear-gradient(90deg,#3a2718,#5a3f28 50%,#3a2718)}
.contact-title{position:absolute;z-index:3;left:0;width:1200px;top:48px;text-align:center;font-family:"Noto Serif",serif;font-weight:400;font-size:42px;color:var(--white);letter-spacing:1px}
.contact-name{position:absolute;left:66px;width:400px;top:120px;text-align:center;font-family:"Cabin",sans-serif;font-size:29px;color:var(--white)}
.contact-blurb{position:absolute;left:80px;width:373px;top:182px;text-align:center;font-family:"Cabin",sans-serif;font-style:italic;font-size:15.5px;line-height:27px;color:var(--white)}
.contact-mail{position:absolute;left:110px;top:398px;display:flex;align-items:center;gap:14px;font-family:"Cabin",sans-serif;font-style:italic;font-size:19px;color:var(--white)}
.social{position:absolute;left:180px;top:455px;display:flex;gap:18px}
.social span{width:45px;height:45px;border-radius:50%;border:2px solid var(--white);display:flex;align-items:center;justify-content:center;font-family:"Cabin",sans-serif;font-size:18px;color:var(--white)}
.social .filled{background:var(--white);color:var(--wood-dark)}
.envelope{position:absolute;z-index:1;left:560px;top:115px;width:470px;height:300px;background:linear-gradient(160deg,#c9b48c,#b0935f);transform:rotate(-10deg)}
.card{position:absolute;z-index:2;left:590px;top:158px;width:543px;height:365px;background:linear-gradient(160deg,#f2e2b8,#dcc08a)}
.form-label,.form-field,.btn-send{z-index:3}
.form-label{position:absolute;left:636px;font-family:"Noto Serif",serif;font-size:17px;color:#1b1b1b}
.form-field{position:absolute;left:721px;width:312px;height:36px;background:var(--white);border:1px solid #c9c0ae}
.btn-send{position:absolute;left:721px;top:418px;width:82px;height:39px;background:linear-gradient(180deg,#ffa22a,var(--orange-dark));color:var(--white);font-weight:700;font-size:17px;display:flex;align-items:center;justify-content:center}

/* footer */
.footer{position:absolute;left:0;top:2218px;width:1200px;height:63px;background:var(--footer);display:flex;align-items:center;justify-content:center;font-family:"Noto Serif",serif;font-weight:700;font-size:13px;color:var(--white)}
.footer .brand-name{color:var(--gold);margin:0 4px;text-transform:uppercase}
</style>
</head>
<body>

<header class="hero">
  <div class="hero-scene" role="img" aria-label="Softly blurred warm background above a wooden tabletop"></div>
  <div class="logo">
    <span class="logo-dot"></span>
    <span class="logo-name">Willow Heart and Soul</span>
  </div>
  <nav class="nav">
    <a class="home" href="#">Home</a>
    <a class="about" href="#">About Dana</a>
    <a class="contact" href="#">Contact</a>
  </nav>
  <div class="book" role="img" aria-label="Two copies of the book Brighten Your Calling standing on the table"></div>
  <h1 class="hero-title">Brighten Your<br>Calling</h1>
  <p class="hero-sub">An Introverts Guide to Creating a Coaching Business that Reflects Who You Are.</p>
  <a class="btn-store"><span class="dot"></span>AVAILABLE ON TELLURIO</a>
</header>

<section class="optin">
  <div class="optin-scene" role="img" aria-label="Man sitting by a lake reading outdoors"></div>
  <h2 class="optin-title">Three Mistakes New Coaches Make While Creating Their Signature Talk.</h2>
  <p class="optin-text">This will help you avoid the most common missteps new coaches make when coming up with their signature message to attract clients</p>
  <div class="pdf-icon" role="img" aria-label="PDF report document"></div>
  <input class="email-field" type="email" placeholder="Enter Your Email*">
  <button class="btn-subscribe">SUBSCRIBE</button>
</section>

<section class="bio">
  <h2 class="bio-title">Meet Dana</h2>
  <div class="bio-text">
    <p>Dana Ellery holds a bachelor’s degree in psychology from Harborview University, giving her a deep understanding of the motivations behind food, career and lifestyle choices. She spent a decade in management with some of the most successful food businesses in the country.</p>
    <p>Dana has helped businesses achieve dramatic improvements in their organization and focus – in turn, making their businesses more profitable. Clients who seek Dana’s guidance are ready to get real and get wise, both in terms of health and business goals. She helps coaches quickly recognize easy to integrate strategies that will suit their work style to help eliminate the confusion on what to do next which in turn will boost their confidence and their bottom line.</p>
    <p>Dana is a classically trained culinary chef from Lindenfield Culinary Institute and a certified raw foods chef, a certified yoga instructor, reiki master, an StillRest facilitator, and a certified Business Coach for Wellness and Artistic Professionals.</p>
  </div>
  <div class="portrait" role="img" aria-label="Portrait photo of Dana Ellery"></div>
</section>

<section class="contact">
  <div class="contact-scene" role="img" aria-label="Dark wooden planks background"></div>
  <h2 class="contact-title">CONTACT ME</h2>
  <p class="contact-name">- &nbsp;Dana Ellery&nbsp; -</p>
  <p class="contact-blurb">founder of Willow Heart and Soul, helps new coaches and creative entrepreneurs find their inner voice so that they have the confidence to bring their authentic selves out into the world. Dana has gone through this process for herself and helped other new businesses achieve dramatic improvements in their organization and focus as a result.</p>
  <div class="contact-mail">
    <svg width="30" height="20" viewBox="0 0 30 20" fill="none" stroke="#fff" stroke-width="1.5"><rect x="1" y="1" width="28" height="18"/><path d="M1 1l14 10L29 1M1 19l10-9M29 19l-10-9"/></svg>
    Dana@BrightenYourCalling.com
  </div>
  <div class="social">
    <span class="filled" aria-label="Chatterloop">c</span>
    <span aria-label="Plusring">p</span>
    <span aria-label="Flitter">f</span>
  </div>
  <div class="envelope" role="img" aria-label="Vintage envelope with floral stamp"></div>
  <div class="card" role="img" aria-label="Aged paper card"></div>
  <span class="form-label" style="top:221px">Name:</span>
  <span class="form-field" style="top:214px"></span>
  <span class="form-label" style="top:261px">E-mail:</span>
  <span class="form-field" style="top:254px"></span>
  <span class="form-label" style="top:300px">Phone:</span>
  <span class="form-field" style="top:293px"></span>
  <span class="form-label" style="top:338px">Message:</span>
  <span class="form-field" style="top:334px;height:72px"></span>
  <span class="btn-send">SEND</span>
</section>

<footer class="footer">© <span class="brand-name">Willow Heart and Soul</span> - 2017. All Rights Reserved.</footer>

</body>
</html>
```